Real Estate - Property Management Business needs a Landlords Handbook designed

We need a landlord's handbook designed. We are a specialist property management business. The text and logos are there. The book needs images and to present more as a book. We would like to see designs that use orange, grey and white.
Our website is www.leasewisegroup.com.au to give you an idea of our brand.

Target Market(s)

Professional couples - property investors

Industry/Entity Type

Real Estate

Font styles to use
Sans Serif

Colors
ffffff
1b1b1b
f37122

Requirements
Must have
• Images of property owners and applicable images
Nice to have
• The Pembertons owner handbook is a guide to show you what I am looking for
Should not have
• This needs to look professional. No cartoon images

```html
<!DOCTYPE html>
<html lang="en">
<head>
<meta charset="utf-8">
<title>What do we do for our management services?</title>
<link href="https://fonts.googleapis.com/css2?family=Arimo:wght@400;700&display=swap" rel="stylesheet">
<style>
  :root{
    --orange:#f37122;
    --ink:#2b2b2b;
    --white:#ffffff;
    --band:#b8b8b8;
    --footer:#3a3a3a;
  }
  *{margin:0;padding:0;box-sizing:border-box}
  html,body{width:848px;height:1200px;overflow:hidden;background:var(--white)}
  body{font-family:"Arimo",Arial,sans-serif;color:var(--ink);position:relative}
  .hero{position:absolute;left:69px;top:40px;width:710px;height:89px;overflow:hidden}
  .hero-photo{position:absolute;inset:0 0 8px 0;
    background:linear-gradient(90deg,#c98f5c 0%,#d6a779 24%,#b9b3a8 32%,#a9a7a2 55%,#bdbbb6 86%,#8a8a6a 100%)}
  .hero-band{position:absolute;left:0;right:0;bottom:0;height:8px;background:var(--band)}
  .hero-title{position:absolute;right:16px;top:14px;color:var(--white);font-weight:400;
    font-size:32px;line-height:30px;text-align:right;letter-spacing:-0.3px}
  .column{position:absolute;top:309px;font-size:13px;line-height:16.8px}
  .column.left{left:69px;width:336px}
  .column.right{left:463px;width:322px}
  .intro{margin-bottom:17px}
  ul{list-style:none}
  .services>li{position:relative;padding-left:20px;margin-bottom:17px}
  .services>li::before{content:"";position:absolute;left:1px;top:6px;width:6px;height:6px;border-radius:50%;background:var(--orange)}
  .details{margin-top:4px}
  .details>li{position:relative;padding-left:20px;margin-bottom:4px}
  .details>li::before{content:"";position:absolute;left:1px;top:6px;width:5px;height:5px;background:var(--ink);transform:rotate(45deg)}
  .notes{margin-top:4px}
  .notes>li{position:relative;padding-left:20px;margin-bottom:4px}
  .notes>li::before{content:"";position:absolute;left:0;top:5px;width:6px;height:6px;border:1px solid var(--ink)}
  .right .services{margin-top:17px}
  .footer{position:absolute;left:0;bottom:0;width:848px;height:40px;background:var(--footer)}
  .footer-label{position:absolute;right:43px;top:12px;font-size:12.8px;color:var(--orange)}
  .footer-label .page{color:var(--white);margin-left:5px}
</style>
</head>
<body>
  <header class="hero">
    <div class="hero-photo" role="img" aria-label="Brick letterbox wall beside a concrete driveway"></div>
    <div class="hero-band"></div>
    <h1 class="hero-title">What do we do for our<br>management services?</h1>
  </header>

  <section class="column left">
    <p class="intro">Our agency manages the tenancy relationship and relevant tenancy matters on your behalf.</p>
    <p class="intro">Below are some of the main services we carry out on your behalf as your managing agent;</p>
    <ul class="services">
      <li>Showing your property
        <ul class="details"><li>Organising inspections to show the property to prospective tenants.</li></ul>
      </li>
      <li>Advertising your property
        <ul class="details"><li>Using resources such as real estate websites and the agency rent list.</li></ul>
      </li>
      <li>Processing tenancy applications
        <ul class="details"><li>Verification and assessment of the tenant’s ability to pay rent and ability to care for the property including tenancy database checks.</li></ul>
      </li>
      <li>Lodging rental bonds to the Government Authority (RLB) on your behalf
        <ul class="details"><li>It is a legal requirement that rental bonds paid by a tenant be paid to the RLB (Residential Leasing Board) within 10 days of monies being received. Bonds can be no more than 4 x the weekly rent if the rental weekly value is $700 per week or less. If the rental property is over $700 per week, the bond total amount is not limited and is negotiable between the parties.</li></ul>
      </li>
      <li>Completion of the required tenancy documents to commence the tenancy on your behalf
        <ul class="details">
          <li>The RLB Form 7c – the General Tenancy Agreement
            <ul class="notes"><li>This must be given to the tenant prior to monies being taken.</li></ul>
          </li>
          <li>The RLB Form 3b – the entry condition report
            <ul class="notes"><li>One copy must be provided to the tenant on or before the day they take possession. The tenant has 3 days in which to sign and return a copy with any additional comments. We will forward a copy to you for your records and discuss any matters if applicable.</li></ul>
          </li>
        </ul>
      </li>
    </ul>
  </section>

  <section class="column right">
    <ul class="details" style="margin-top:0;margin-left:-20px">
      <li>The RLB Form 5d – the Information Statement
        <ul class="notes"><li>A guide to renting booklet provided by the RLB that we on your behalf a required to provide to tenant when giving the agreement for signing (a copy is provided as part of this guide package). The booklet is required by law to be given to tenants when the agreement is given for signing.</li></ul>
      </li>
      <li>Body corporate by-laws (if applicable)
        <ul class="notes"><li>Our agency on your behalf, provide the body corporate by laws (if applicable) to your tenants in compliance with legislative requirements. It is a legal requirement that body corporate by laws be given to tenants when the tenancy agreement is given for signing.</li></ul>
      </li>
      <li>Trust account receipt for rent and bond monies paid
        <ul class="notes">
          <li>Lodge the bond with the Government authority as required by law.</li>
          <li>RLB Form 9 – bond lodgement form completed and lodged with Government.</li>
        </ul>
      </li>
    </ul>
    <ul class="services" style="margin-left:-20px">
      <li>Accounting on your behalf
        <ul class="details">
          <li>Payment of invoices for maintenance and other instructed matters.</li>
          <li>Disbursement of rental trust funds.</li>
        </ul>
      </li>
      <li>Rent arrears
        <ul class="details">
          <li>Daily rent arrears administration and monitoring.</li>
          <li>Issuing of required statutory notices as required and if applicable.</li>
          <li>Communication with the tenant and the lessor as required.</li>
        </ul>
      </li>
      <li>Maintenance negotiation
        <ul class="details">
          <li>Notifying the lessor of maintenance (as per management agreement instructions)</li>
          <li>Communication with the tenant</li>
          <li>Organising a suitable contractor</li>
          <li>Providing a work order to the contractor</li>
          <li>Following up as required</li>
          <li>Payment of invoice</li>
          <li>Accounting to the lessor accordingly.</li>
        </ul>
      </li>
    </ul>
  </section>

  <footer class="footer">
    <p class="footer-label">Harbourline Rentals<span class="page">5</span></p>
  </footer>
</body>
</html>
```